" ATENDEMOS CLIENTES DE BALCÃO PARA VENDA DE PEÇAS E PNEUS DA LINHA LEVE + CAMIONETES NACIONAIS E IMPORTADOS. CONTAMOS COM UM CENTRO AUTOMOTIVO DE GRANDE PORTE PARA EXECUTAR SERVIÇOS MECÂNICOS DE REVISÃO E MANUTENÇÃO CORRETIVA E PREVENTIVA ( ALINHAMENTO, BALANCEAMENTO, MONTAGEM DE PNEUS, SUSPENSÃO, FREIOS, CAMBIO MANUAL E AUTOMATIZADO, INJEÇÃO ELETRÔNICA, REPARO DE MOTOR E CABEÇOTES, SISTEMA DE DIREÇÃO ). "

```html
<!DOCTYPE html>
<html lang="pt-BR">
<head>
<meta charset="UTF-8">
<title>Crachá de identificação</title>
<link rel="stylesheet" href="https://fonts.googleapis.com/css2?family=Montserrat:wght@400;500;600;700;800&display=swap">
<style>
  :root {
    --bg: #1f2328;
    --card: #ffffff;
    --ink: #2a2d31;
    --muted: #8a8f96;
    --line: #b9bdc2;
    --red: #e3141b;
  }
  * { margin: 0; padding: 0; box-sizing: border-box; }
  html, body {
    width: 1200px;
    height: 1200px;
    overflow: hidden;
    background: var(--bg);
    font-family: "Montserrat", sans-serif;
  }
  .stage {
    width: 1200px;
    height: 1200px;
    display: flex;
    align-items: center;
    justify-content: center;
  }
  .badge {
    position: relative;
    width: 580px;
    height: 860px;
    background: var(--card);
    border-radius: 22px;
    padding: 150px 60px 70px;
    display: flex;
    flex-direction: column;
    color: var(--ink);
  }
  .badge-slot {
    position: absolute;
    top: 48px;
    left: 50%;
    transform: translateX(-50%);
    width: 120px;
    height: 22px;
    border-radius: 11px;
    background: var(--bg);
  }
  .field { margin-bottom: 26px; }
  .field-label {
    display: block;
    font-size: 17px;
    font-weight: 500;
    color: var(--muted);
    margin: 0 0 4px 14px;
  }
  .field-box {
    border: 2px solid var(--line);
    border-radius: 12px;
    padding: 12px 16px;
    text-align: center;
    font-size: 22px;
    font-weight: 700;
    letter-spacing: 0.5px;
    line-height: 1.2;
  }
  .field-box .role { display: block; font-size: 20px; }
  .notice {
    margin-top: 22px;
    text-align: center;
    font-size: 15px;
    font-weight: 500;
    line-height: 1.55;
    letter-spacing: 0.4px;
    text-transform: uppercase;
  }
  .brand {
    margin-top: auto;
    display: flex;
    align-items: center;
    justify-content: center;
    gap: 14px;
  }
  .brand-mark {
    width: 18px;
    height: 18px;
    background: var(--red);
  }
  .brand-name {
    font-size: 36px;
    font-weight: 700;
    color: var(--ink);
    letter-spacing: 2px;
  }
</style>
</head>
<body>
<main class="stage">
  <article class="badge">
    <span class="badge-slot"></span>

    <div class="field">
      <span class="field-label">Nome</span>
      <div class="field-box">NOME SOBRENOME<span class="role">CARGO</span></div>
    </div>

    <div class="field">
      <span class="field-label">RG</span>
      <div class="field-box">00.000.000-00</div>
    </div>

    <div class="field">
      <span class="field-label">CPF</span>
      <div class="field-box">000.000.000-00</div>
    </div>

    <p class="notice">
      Este crachá é de uso pessoal<br>
      e obrigatório o uso durante a sua<br>
      permanência na empresa.<br>
      Em caso de perda ou extravio<br>
      comunique imediatamente a área de<br>
      recursos humanos.
    </p>

    <div class="brand">
      <span class="brand-mark"></span>
      <span class="brand-name">VALEMAR PNEUS</span>
    </div>
  </article>
</main>
</body>
</html>
```